Veterinary Business cards

Redesign Business Card

Information needed on Card:
Hours: Mon-Fri: 4pm -10PM; Sat- Sun- 10 AM- 5PM
Help@tandrelyns.com
www.tandrelyns.com
405-718-2954
4170 SW 38th Ave. okc, ok 73119
*No appointment necessary*

Optional:
Our tag line is "We're here when you need us" - If it fits on the cards.

```html
<!DOCTYPE html>
<html lang="en">
<head>
<meta charset="utf-8">
<title>Tandrelyn Urgent Care – Business Card</title>
<link href="https://fonts.googleapis.com/css2?family=Montserrat:wght@400;500;600;700&display=swap" rel="stylesheet">
<style>
  :root {
    --navy: #173a66;
    --orange: #d97b1f;
    --white: #ffffff;
    --ink: #1f2a3a;
    --backdrop: #2b2b2b;
  }
  * { box-sizing: border-box; margin: 0; padding: 0; }
  html, body { width: 1200px; height: 1186px; overflow: hidden; }
  body {
    background: var(--backdrop);
    font-family: "Montserrat", sans-serif;
    position: relative;
  }
  .card {
    position: absolute;
    left: 240px;
    width: 720px;
    height: 410px;
    border-radius: 26px;
    overflow: hidden;
  }
  .card-back { top: 110px; background: var(--navy); }
  .card-front { top: 666px; background: var(--white); }

  .brand {
    position: absolute;
    display: flex;
    align-items: center;
    gap: 18px;
    font-weight: 600;
    letter-spacing: 0.06em;
    text-transform: uppercase;
    line-height: 1.05;
  }
  .brand-dot { width: 30px; height: 30px; border-radius: 50%; background: var(--orange); flex: none; }
  .card-back .brand { left: 50%; top: 50%; transform: translate(-50%, -50%); color: var(--white); font-size: 52px; }
  .card-back .brand small { display: block; font-size: 28px; letter-spacing: 0.2em; font-weight: 600; }
  .card-front .brand { left: 42px; top: 74px; color: var(--navy); font-size: 34px; }
  .card-front .brand small { display: block; font-size: 18px; letter-spacing: 0.2em; font-weight: 600; }
  .card-front .brand-dot { width: 22px; height: 22px; }

  .rule { position: absolute; left: 340px; right: 30px; top: 150px; height: 2px; background: var(--orange); }

  .hours {
    position: absolute;
    left: 480px; top: 172px;
    padding-left: 14px;
    border-left: 3px solid var(--orange);
    font-size: 15px; color: var(--ink); line-height: 1.3;
  }
  .hours h3 { color: var(--orange); font-size: 18px; font-weight: 700; }

  .band { position: absolute; inset: 0; }
  .band-note {
    position: absolute; right: 34px; top: 322px;
    color: var(--white); font-size: 15px; font-weight: 500;
  }

  .contact { position: absolute; left: 42px; top: 214px; list-style: none; font-size: 16px; color: var(--ink); }
  .contact li { display: flex; align-items: center; gap: 12px; height: 27px; }
  .contact li:first-child { margin-bottom: 10px; }
  .contact svg { width: 14px; height: 14px; fill: var(--orange); flex: none; }
</style>
</head>
<body>

<section class="card card-back">
  <div class="brand">
    <span class="brand-dot"></span>
    <span>Tandrelyn<small>Urgent Care</small></span>
  </div>
</section>

<section class="card card-front">
  <svg class="band" viewBox="0 0 720 410" aria-hidden="true">
    <path d="M0 338 H456 L446 354 H0 Z" fill="var(--orange)"/>
    <path d="M0 366 H452 Q462 366 464 356 L470 292 Q472 280 484 280 H720 V410 H0 Z" fill="var(--navy)"/>
  </svg>

  <div class="brand">
    <span class="brand-dot"></span>
    <span>Tandrelyn<small>Urgent Care</small></span>
  </div>

  <div class="rule"></div>

  <div class="hours">
    <h3>Hours</h3>
    <p>Mon-Fri: 4pm -10PM</p>
    <p>Sat- Sun- 10 AM- 5PM</p>
  </div>

  <p class="band-note">No appointment necessary</p>

  <ul class="contact">
    <li>
      <svg viewBox="0 0 24 24"><path d="M12 2a7 7 0 0 0-7 7c0 5 7 13 7 13s7-8 7-13a7 7 0 0 0-7-7zm0 9.5A2.5 2.5 0 1 1 12 6.5a2.5 2.5 0 0 1 0 5z"/></svg>
      4170 SW 38th Ave. okc, ok 73119
    </li>
    <li>
      <svg viewBox="0 0 24 24"><path d="M6.6 10.8a15 15 0 0 0 6.6 6.6l2.2-2.2a1 1 0 0 1 1-.25 11.4 11.4 0 0 0 3.6.57 1 1 0 0 1 1 1V20a1 1 0 0 1-1 1A17 17 0 0 1 3 4a1 1 0 0 1 1-1h3.5a1 1 0 0 1 1 1c0 1.25.2 2.45.57 3.57a1 1 0 0 1-.25 1z"/></svg>
      405-718-2954
    </li>
    <li>
      <svg viewBox="0 0 24 24"><path d="M2 5h20v14H2z M2 5l10 8 10-8" fill="var(--orange)"/></svg>
      Help@tandrelyns.com
    </li>
    <li>
      <svg viewBox="0 0 24 24"><circle cx="12" cy="12" r="10"/></svg>
      www.tandrelyns.com
    </li>
  </ul>
</section>

</body>
</html>
```